I need a business card design for a new company that will be doing consulting work around issues of cultural competency, and diversity and inclusion. I would like the design to be crisp and clear with bold but conservative colors and incorporate shades of blue

Target Market(s)

Small businesses, schools, non-profits

Industry/Entity Type

Consulting

Font styles to use
Serif
Sans Serif

Colors
0c5ba6
6b449b
3276b5
0292cd

Requirements
Must have
• A Morrow Venture (name of company)
• Lemlem Tavish
• CEO
• lemlem@amorrowventure.com
• (215)483-2756

```html
<!DOCTYPE html>
<html lang="en">
<head>
<meta charset="utf-8">
<title>A Morrow Venture — Business Card</title>
<link rel="stylesheet" href="https://fonts.googleapis.com/css2?family=Open+Sans:wght@400;600;700&display=swap">
<style>
  :root {
    --page-bg: #e9e6e1;
    --card-blue: #0c5ba6;
    --accent-purple: #6b449b;
    --mid-blue: #3276b5;
    --bright-blue: #0292cd;
    --name-blue: #1fa3e3;
    --text-white: #ffffff;
  }
  * { box-sizing: border-box; margin: 0; padding: 0; }
  html, body {
    width: 1200px;
    height: 815px;
    overflow: hidden;
    background: var(--page-bg);
    font-family: "Open Sans", Arial, sans-serif;
  }
  .canvas {
    width: 1200px;
    height: 815px;
    display: flex;
    align-items: center;
    justify-content: center;
  }
  .business-card {
    position: relative;
    width: 900px;
    height: 514px;
    background: var(--card-blue);
    box-shadow: 0 10px 30px rgba(0, 0, 0, 0.18);
    overflow: hidden;
  }
  .bottom-band {
    position: absolute;
    left: 0;
    right: 0;
    bottom: 0;
    height: 16px;
    background: var(--accent-purple);
  }
  .brand-name {
    position: absolute;
    left: 70px;
    top: 205px;
    width: 300px;
    text-align: center;
    color: var(--text-white);
    font-weight: 700;
    font-size: 38px;
    line-height: 1.15;
    letter-spacing: 0.3px;
  }
  .divider {
    position: absolute;
    left: 400px;
    top: 78px;
    width: 3px;
    height: 330px;
    background: var(--bright-blue);
  }
  .person-name {
    position: absolute;
    left: 440px;
    top: 80px;
    color: var(--name-blue);
    font-weight: 700;
    font-size: 33px;
    letter-spacing: 0.5px;
    text-transform: uppercase;
  }
  .person-title {
    position: absolute;
    left: 440px;
    top: 128px;
    color: var(--text-white);
    font-weight: 600;
    font-size: 15px;
  }
  .contact-list {
    position: absolute;
    left: 430px;
    top: 318px;
    list-style: none;
  }
  .contact-item {
    display: flex;
    align-items: center;
    gap: 12px;
    color: var(--text-white);
    font-weight: 600;
    font-size: 22px;
    letter-spacing: 0.4px;
    height: 40px;
  }
  .contact-icon {
    width: 20px;
    height: 20px;
    flex: none;
  }
</style>
</head>
<body>
  <main class="canvas">
    <article class="business-card">
      <div class="brand-name">A Morrow<br>Venture</div>
      <div class="divider"></div>

      <h1 class="person-name">Lemlem Tavish</h1>
      <p class="person-title">CEO</p>

      <ul class="contact-list">
        <li class="contact-item">
          <svg class="contact-icon" viewBox="0 0 20 20" aria-hidden="true">
            <circle cx="10" cy="10" r="8.5" fill="none" stroke="var(--name-blue)" stroke-width="1.4"/>
            <path d="M7 5.5 l1.6 0 l0.8 2.2 l-1 0.8 a5 5 0 0 0 2.6 2.6 l0.8 -1 l2.2 0.8 l0 1.6 a1 1 0 0 1 -1 1 a8 8 0 0 1 -7 -7 a1 1 0 0 1 1 -1z" fill="var(--name-blue)"/>
          </svg>
          <span>(215)483-2756</span>
        </li>
        <li class="contact-item">
          <svg class="contact-icon" viewBox="0 0 20 20" aria-hidden="true">
            <circle cx="10" cy="10" r="8.5" fill="none" stroke="var(--name-blue)" stroke-width="1.4"/>
            <ellipse cx="10" cy="10" rx="3.5" ry="8.5" fill="none" stroke="var(--name-blue)" stroke-width="1.2"/>
            <line x1="1.5" y1="10" x2="18.5" y2="10" stroke="var(--name-blue)" stroke-width="1.2"/>
          </svg>
          <span>lemlem@amorrowventure.com</span>
        </li>
      </ul>

      <div class="bottom-band"></div>
    </article>
  </main>
</body>
</html>
```